Author Personal Brand Wordpress Design

I need a wordpress theme to rebrand my website. I am an author who writes both romance and fantasy novels and therefore want a brand that will represent my style of writing which is warm, emotional and adventurous.

My name should be across the top (Maren Holt). Font used should be modern, easy-to-read and fun. My preference is towards handwritten fonts, but this is not essential.

Colours should be cheerful, vibrant and light (no dark backgrounds please) - maybe reds and yellows (but not essential - use your imagination). Images can be used.

The final design should communicate approachable, warm and positive.

The designers should keep in mind that elements of the final design should be able to be incorporated into a stationery suite (letterhead, business cards, email signature, powerpoint and with compliments slip) and the header should be able to be resized for an email newsletter (PostLark), and Chirply/Frendbook.

The website design must be responsive, and take the full width of the page (see the Pellucid theme or Driftwick theme for an example of what I mean). Social media icons must be able to be installed and used and the menu should run horizontally across the page. My preference is to be able to have multiple sidebars (one for blog and one for the rest of the site), and a sticky menu.

I need to be able to install the design into Wordpress and I can create additional pages from there. See my current website www.marenholt-example.com for examples of content.

Final Product:
- Wordpress web design I can install myself
- Header image which can be resized for newsletter, Frendbook and Chirply
- Name of font used (must be one I have access to eg: can purchase)
- List of colours used

Target Market(s)

Women 25-50

Industry/Entity Type

Business

Requirements
Must have
• Responsive, full width, social media icons (preferably at the top of the page)
Nice to have
• Sticky menu, accessibility
Should not have
• No couples embracing, or holding hands. The design should not be about the romance genre as I will be writing fantasy this year.

```html
<!DOCTYPE html>
<html lang="en">
<head>
<meta charset="utf-8">
<title>Maren Holt — Author</title>
<link href="https://fonts.googleapis.com/css2?family=Cousine&family=PT+Serif:ital,wght@0,400;0,700;1,400&display=swap" rel="stylesheet">
<style>
  :root {
    --page: #ffffff;
    --ink: #2f2f2f;
    --brand-blue: #4b8cb9;
    --social-grey: #b9b9b9;
    --topbar: #ebebeb;
    --dark-band: #3e3e3e;
    --panel: #f3f2f3;
    --footer: #f0f0f0;
    --pink: #e6507f;
    --magenta: #d63c86;
    --purple: #8b3aa0;
    --violet: #a84ef5;
    --sky: #2f86dd;
    --book-yellow: #f7c958;
    --book-orange: #ee8e6a;
    --book-grey: #979695;
    --frame: #e3e3e3;
  }
  * { box-sizing: border-box; margin: 0; padding: 0; }
  html, body { width: 858px; height: 1200px; overflow: hidden; background: var(--page); }
  body { position: relative; font-family: "PT Serif", Georgia, serif; color: var(--ink); }

  .top-bar { position: absolute; left: 126px; top: 10px; width: 498px; height: 21px; background: var(--topbar); display: flex; justify-content: center; align-items: center; gap: 4px; }
  .social-dot { width: 9px; height: 9px; border-radius: 50%; background: var(--social-grey); }

  .corner-left { position: absolute; left: 12px; top: 10px; width: 148px; height: 186px; background: linear-gradient(160deg, var(--purple) 0%, var(--magenta) 50%, var(--pink) 100%); }
  .corner-right { position: absolute; left: 624px; top: 10px; width: 226px; height: 34px; background: var(--sky); }
  .header-photo { position: absolute; left: 644px; top: 44px; width: 206px; height: 152px; background: linear-gradient(180deg, #c9b7a6 0%, #e4c8a4 45%, #8d8a8e 75%, #5f6a78 100%); }

  .site-title { position: absolute; left: 0; width: 858px; top: 58px; text-align: center; font-family: "PT Serif", Georgia, serif; font-weight: 700; font-size: 30px; line-height: 36px; color: var(--brand-blue); }
  .main-nav { position: absolute; left: 0; width: 858px; top: 113px; display: flex; justify-content: center; gap: 11px; font-family: "Cousine", monospace; font-size: 13px; color: var(--ink); }

  .book-frame { position: absolute; background: #fff; border: 1px solid var(--frame); box-shadow: 0 1px 3px rgba(0,0,0,.08); }
  .book-card { position: absolute; display: flex; flex-direction: column; justify-content: center; align-items: center; text-align: center; }
  .book-card .title { color: #333; }
  .book-card .byline { font-style: italic; color: #444; }
  .feature .title { font-size: 15px; }
  .feature .byline { font-size: 7px; margin-top: 3px; }
  .feature-cover { position: absolute; left: 350px; top: 152px; width: 155px; height: 244px; background: linear-gradient(160deg, #8a7b75 0%, #4b3c39 55%, #1e1716 100%); }
  .arrow { position: absolute; }

  .quote { position: absolute; left: 250px; width: 360px; top: 421px; text-align: center; font-style: italic; font-size: 11.5px; line-height: 19px; color: var(--ink); }
  .quote-source { position: absolute; left: 480px; top: 462px; width: 126px; text-align: right; font-style: italic; font-size: 7px; color: var(--ink); }

  .promo-band { position: absolute; left: 140px; top: 493px; width: 578px; height: 102px; background: var(--dark-band); }
  .promo-text { position: absolute; left: 34px; top: 33px; width: 360px; color: #fff; font-size: 11.5px; line-height: 19px; }
  .promo-button { position: absolute; left: 414px; top: 36px; width: 131px; height: 30px; border: 2px solid #fff; color: #fff; font-weight: 700; font-size: 11px; display: flex; justify-content: center; align-items: center; }

  .section-title { position: absolute; left: 0; width: 858px; text-align: center; font-weight: 700; font-size: 13px; }
  .section-title::after { content: ""; display: block; width: 12px; height: 1px; background: #bdbdbd; margin: 9px auto 0; }

  .books-panel { position: absolute; left: 140px; top: 605px; width: 578px; height: 257px; background: var(--panel); }
  .shelf-book { width: 84px; height: 132px; top: 680px; border: 2px solid #fff; box-shadow: 0 1px 3px rgba(0,0,0,.1); }
  .shelf-book .title { font-size: 9px; }
  .shelf-book .byline { font-size: 5px; margin-top: 3px; }

  .blog-post { position: absolute; width: 260px; height: 56px; }
  .post-date { position: absolute; left: 0; top: 0; width: 55px; height: 55px; background: var(--dark-band); color: #fff; text-align: center; font-weight: 700; }
  .post-date .day { display: block; font-size: 22px; line-height: 24px; padding-top: 5px; }
  .post-date .month { display: block; font-size: 13px; line-height: 15px; }
  .post-body { position: absolute; left: 64px; top: -3px; width: 214px; }
  .post-title { font-weight: 700; font-size: 10px; line-height: 14px; }
  .post-excerpt { font-size: 8.5px; line-height: 12px; color: var(--ink); }

  .site-footer { position: absolute; left: 12px; top: 1138px; width: 838px; height: 50px; background: var(--footer); }
  .copyright { position: absolute; left: 58px; top: 20px; font-family: "Cousine", monospace; font-size: 7px; color: var(--ink); }
  .footer-social { position: absolute; right: 14px; top: 21px; display: flex; gap: 3px; }
</style>
</head>
<body>

  <div class="corner-left" role="img" aria-label="Decorative colour block in pink and purple tones"></div>

  <header>
    <div class="top-bar">
      <span class="social-dot"></span><span class="social-dot"></span><span class="social-dot"></span>
      <span class="social-dot"></span><span class="social-dot"></span><span class="social-dot"></span><span class="social-dot"></span>
    </div>
    <div class="corner-right" role="img" aria-label="Decorative blue colour block"></div>
    <div class="header-photo" role="img" aria-label="Header photograph of a sunset beach"></div>
    <div class="site-title">Maren Holt</div>
    <nav class="main-nav">
      <span>Home</span><span>Bio</span><span>Books</span><span>Memberships</span><span>Media</span><span>Contact</span>
    </nav>
  </header>

  <main>
    <section class="book-carousel">
      <svg class="arrow" style="left:149px;top:298px" width="10" height="14" viewBox="0 0 10 14" aria-hidden="true"><polyline points="8,1 2,7 8,13" fill="none" stroke="#cfcfcf" stroke-width="2"/></svg>
      <div class="book-frame" style="left:217px;top:192px;width:128px;height:210px"></div>
      <div class="book-card feature" style="left:223px;top:200px;width:121px;height:194px;background:var(--violet)">
        <span class="title">Book Title</span><span class="byline">by A.N. Author</span>
      </div>
      <div class="book-frame" style="left:512px;top:192px;width:128px;height:210px"></div>
      <div class="book-card feature" style="left:512px;top:200px;width:121px;height:194px;background:var(--pink)">
        <span class="title">Book Title</span><span class="byline">by A.N. Author</span>
      </div>
      <div class="book-frame" style="left:344px;top:145px;width:168px;height:256px"></div>
      <div class="feature-cover" role="img" aria-label="Featured book cover with guitarist on stage and title lettering"></div>
      <svg class="arrow" style="left:699px;top:298px" width="10" height="14" viewBox="0 0 10 14" aria-hidden="true"><polyline points="2,1 8,7 2,13" fill="none" stroke="#cfcfcf" stroke-width="2"/></svg>
    </section>

    <blockquote class="quote">The best time to take action toward a dream is yesterday; the worst is tomorrow; the best compromise is today.</blockquote>
    <p class="quote-source">- Edda Marlowe, Author</p>

    <section class="promo-band">
      <p class="promo-text">Book 9 is a tail of epic proportions, at only $20 in paperback it really is quite a steal! So come on, what are you waiting for?</p>
      <span class="promo-button">Take me Home Today</span>
    </section>

    <section>
      <div class="books-panel"></div>
      <h2 class="section-title" style="top:632px">My Books</h2>
      <svg class="arrow" style="left:168px;top:743px" width="10" height="14" viewBox="0 0 10 14" aria-hidden="true"><polyline points="8,1 2,7 8,13" fill="none" stroke="#cfcfcf" stroke-width="2"/></svg>
      <div class="book-card shelf-book" style="left:188px;background:var(--book-yellow)"><span class="title">Book Title</span><span class="byline">by A.N. Author</span></div>
      <div class="book-card shelf-book" style="left:287px;background:var(--violet)"><span class="title">Book Title</span><span class="byline">by A.N. Author</span></div>
      <div class="book-card shelf-book" style="left:386px;background:var(--pink)"><span class="title">Book Title</span><span class="byline">by A.N. Author</span></div>
      <div class="book-card shelf-book" style="left:485px;background:var(--book-orange)"><span class="title">Book Title</span><span class="byline">by A.N. Author</span></div>
      <div class="book-card shelf-book" style="left:584px;background:var(--book-grey)"><span class="title">Book Title</span><span class="byline">by A.N. Author</span></div>
      <svg class="arrow" style="left:681px;top:743px" width="10" height="14" viewBox="0 0 10 14" aria-hidden="true"><polyline points="2,1 8,7 2,13" fill="none" stroke="#cfcfcf" stroke-width="2"/></svg>
    </section>

    <section>
      <h2 class="section-title" style="top:889px">My Blog</h2>

      <article class="blog-post" style="left:152px;top:934px">
        <div class="post-date"><span class="day">22</span><span class="month">SEP</span></div>
        <div class="post-body"><h3 class="post-title">The Library</h3><p class="post-excerpt">This is how my library is looking. Lorem ipsum dolor sit amet, consectetur adipiscing elit. Fusce at risus at lacus…</p></div>
      </article>
      <article class="blog-post" style="left:152px;top:994px">
        <div class="post-date"><span class="day">23</span><span class="month">JUL</span></div>
        <div class="post-body"><h3 class="post-title">Creating a Video</h3><p class="post-excerpt">I've been looking into creating a video to advertise my latest book. Lorem ipsum dolor sit amet, consectetur adipiscing elit….</p></div>
      </article>
      <article class="blog-post" style="left:152px;top:1055px">
        <div class="post-date"><span class="day">19</span><span class="month">JAN</span></div>
        <div class="post-body"><h3 class="post-title">My first book</h3><p class="post-excerpt">This is how I started on my first book, retro. Lorem ipsum dolor sit amet, consectetur adipiscing elit. Fusce at…</p></div>
      </article>

      <article class="blog-post" style="left:440px;top:934px">
        <div class="post-date"><span class="day">08</span><span class="month">AUG</span></div>
        <div class="post-body"><h3 class="post-title">My first podcast</h3><p class="post-excerpt">I've recorded one of those podcast things! Lorem ipsum dolor sit amet, consectetur adipiscing elit. Fusce at risus at lacus…</p></div>
      </article>
      <article class="blog-post" style="left:440px;top:994px">
        <div class="post-date"><span class="day">05</span><span class="month">FEB</span></div>
        <div class="post-body"><h3 class="post-title">I bought a camera</h3><p class="post-excerpt">I've finally bought a camera and have been testing it out. Lorem ipsum dolor sit amet, consectetur adipiscing elit. Fusce…</p></div>
      </article>
      <article class="blog-post" style="left:440px;top:1055px">
        <div class="post-date"><span class="day">23</span><span class="month">SEP</span></div>
        <div class="post-body"><h3 class="post-title">What a Quote</h3><p class="post-excerpt">Keep reading books, but remember that a book is only a book, and you should learn to think for yourself.</p></div>
      </article>
    </section>
  </main>

  <footer class="site-footer">
    <p class="copyright">copyright 2015</p>
    <div class="footer-social">
      <span class="social-dot"></span><span class="social-dot"></span><span class="social-dot"></span>
      <span class="social-dot"></span><span class="social-dot"></span><span class="social-dot"></span><span class="social-dot"></span>
    </div>
  </footer>

</body>
</html>
```